Advertisement Design Project

I need a half page advert to be designed to appear in a magazine titled The Prudent Nest Ledger that focuses on finance and self-managed superannuation in Australia.
My client has provided a mock advert with the content that they would like jazzed up to a more professional feel.
Below is a link to view a previous copy of the magazine the advert will be appearing in.
http://www.brackenpress.com.au/PNLmagazine/pnlwin12-13/index.html
Please dont hesitate to contact me if you have any questions.
Thanks
Doug Ferrow
Target Market(s)
Investors, aged 40-70
Industry/Entity Type
Finance
Look and feel

```html
<!DOCTYPE html>
<html lang="en">
<head>
<meta charset="utf-8">
<title>Harbourline Property – Half Page Advert</title>
<link href="https://fonts.googleapis.com/css2?family=Archivo+Black&family=Archivo:ital,wght@0,400;0,700;0,800;1,700&display=swap" rel="stylesheet">
<style>
  :root {
    --charcoal: #2e2c2d;
    --red: #e01f26;
    --red-dark: #a5141a;
    --yellow: #ffe600;
    --white: #ffffff;
    --blue: #1f4f9c;
    --backdrop: #d6d6d6;
    --sky-top: #7ea6d6;
    --sky-mid: #cfdcec;
    --grass: #4f8f2c;
  }
  * { box-sizing: border-box; margin: 0; padding: 0; }
  html, body { width: 1200px; height: 1000px; overflow: hidden; }
  body { background: var(--backdrop); font-family: "Archivo", Arial, sans-serif; }

  .advert {
    position: absolute; left: 134px; top: 142px;
    width: 942px; height: 690px; background: var(--charcoal); overflow: hidden;
  }
  .headline-bar {
    height: 48px; display: flex; align-items: center; justify-content: center;
    color: var(--white); font-family: "Archivo Black", Arial, sans-serif;
    font-size: 28px; letter-spacing: 1.5px;
  }
  .offer-band {
    height: 92px; background: linear-gradient(#ee2a30, var(--red) 60%, #c5181e);
    display: flex; align-items: center; padding-left: 14px;
  }
  .offer-amount {
    font-family: "Archivo Black", Arial, sans-serif; font-size: 74px;
    color: var(--white); letter-spacing: 1px; text-shadow: 3px 3px 3px rgba(0,0,0,.45);
  }
  .offer-schemes {
    margin-left: 22px; font-family: "Archivo Black", Arial, sans-serif;
    font-size: 31px; line-height: 30px; color: var(--yellow);
    text-shadow: 2px 2px 2px rgba(0,0,0,.4);
  }
  .intro-band {
    height: 80px; display: flex; align-items: center; justify-content: center;
    text-align: center; color: var(--white); font-weight: 800;
    font-size: 25px; line-height: 31px; letter-spacing: 1.2px;
  }
  .hero {
    position: absolute; left: 0; top: 220px; width: 942px; height: 428px;
    background: linear-gradient(180deg, var(--sky-top) 0%, var(--sky-mid) 45%, #e8e2d4 62%, #b9ac93 72%, var(--grass) 78%, #3f7a22 100%);
  }
  .region-list {
    position: absolute; left: 140px; top: 235px;
    display: grid; grid-template-columns: 324px 330px; row-gap: 4px;
    list-style: none; color: var(--blue); font-weight: 800;
    font-size: 18px; letter-spacing: .8px;
  }
  .region-list li { display: flex; align-items: center; gap: 7px; height: 20px; }
  .region-list svg { width: 19px; height: 17px; flex: none; }

  .brand { position: absolute; left: 26px; top: 530px; }
  .brand-name { display: flex; align-items: center; gap: 10px;
    font-weight: 800; font-style: italic; font-size: 16px; color: #111; }
  .brand-mark { width: 16px; height: 16px; background: var(--red); }
  .brand-tagline { margin-top: 3px; margin-left: 26px; font-size: 17px; font-style: italic; color: #111; }
  .brand-tagline em { color: var(--red); font-weight: 800; }
  .brand-web { margin-top: 14px; font-weight: 800; font-size: 21px; color: var(--white); letter-spacing: .5px;
    text-shadow: 1px 1px 2px rgba(0,0,0,.5); }

  .contact-band {
    position: absolute; left: 426px; top: 520px; width: 516px; height: 114px;
    background: linear-gradient(90deg, var(--red), #d81c22 70%, #b5161c);
  }
  .contact-tab {
    position: absolute; left: 0; top: 0; width: 30px; height: 114px; background: var(--red-dark);
    display: flex; align-items: center; justify-content: center;
  }
  .contact-tab span { transform: rotate(-90deg); color: var(--white); font-weight: 800; font-size: 15px; letter-spacing: 1.5px; }
  .portrait {
    position: absolute; left: 464px; top: 513px; width: 108px; height: 125px;
    background: linear-gradient(#c9c2b4, #8e877c 60%, #2a2d3a); border: 2px solid #222;
  }
  .contact-details { position: absolute; left: 597px; top: 525px; color: var(--white); }
  .contact-name { font-weight: 800; font-size: 21px; letter-spacing: .5px; }
  .contact-role { font-weight: 700; font-size: 12px; color: #111; margin-bottom: 6px; }
  .contact-row { font-weight: 700; font-size: 16px; line-height: 20px; letter-spacing: .5px; }
  .contact-row b { color: #111; font-weight: 700; }

  .cta-bar {
    position: absolute; left: 0; bottom: 0; width: 942px; height: 42px;
    display: flex; align-items: center; justify-content: center;
    color: var(--white); font-weight: 800; font-size: 19px; letter-spacing: 1px;
  }
</style>
</head>
<body>
<main class="advert">
  <div class="headline-bar">RECEIVE - TAX FREE FROM THE GOVERNMENT</div>
  <div class="offer-band">
    <span class="offer-amount">Over $100,000</span>
    <span class="offer-schemes">NRAS &amp;<br>SMSFs</span>
  </div>
  <div class="intro-band">Choose from the best range of HIGH CASHFLOW<br>properties in Queensland from $275,000 in:</div>

  <div class="hero" role="img" aria-label="Photo of a modern single-storey brick house with double garage under a cloudy blue sky, front lawn"></div>

  <ul class="region-list">
    <li><svg viewBox="0 0 19 17"><rect x="1" y="3" width="12" height="12" fill="#fff" stroke="#e01f26" stroke-width="1.5"/><path d="M4 9l3 3 10-11" fill="none" stroke="#e01f26" stroke-width="3"/></svg>BRISBANE &amp; IPSWICH</li>
    <li><svg viewBox="0 0 19 17"><rect x="1" y="3" width="12" height="12" fill="#fff" stroke="#e01f26" stroke-width="1.5"/><path d="M4 9l3 3 10-11" fill="none" stroke="#e01f26" stroke-width="3"/></svg>GLADSTONE/ROCKHAMPTON</li>
    <li><svg viewBox="0 0 19 17"><rect x="1" y="3" width="12" height="12" fill="#fff" stroke="#e01f26" stroke-width="1.5"/><path d="M4 9l3 3 10-11" fill="none" stroke="#e01f26" stroke-width="3"/></svg>MORETON BAY REGION</li>
    <li><svg viewBox="0 0 19 17"><rect x="1" y="3" width="12" height="12" fill="#fff" stroke="#e01f26" stroke-width="1.5"/><path d="M4 9l3 3 10-11" fill="none" stroke="#e01f26" stroke-width="3"/></svg>GOLD &amp; SUNSHINE COASTS</li>
    <li><svg viewBox="0 0 19 17"><rect x="1" y="3" width="12" height="12" fill="#fff" stroke="#e01f26" stroke-width="1.5"/><path d="M4 9l3 3 10-11" fill="none" stroke="#e01f26" stroke-width="3"/></svg>LOGAN &amp; SCENIC RIM</li>
    <li><svg viewBox="0 0 19 17"><rect x="1" y="3" width="12" height="12" fill="#fff" stroke="#e01f26" stroke-width="1.5"/><path d="M4 9l3 3 10-11" fill="none" stroke="#e01f26" stroke-width="3"/></svg>TOWNSVILLE &amp; MINING</li>
    <li><svg viewBox="0 0 19 17"><rect x="1" y="3" width="12" height="12" fill="#fff" stroke="#e01f26" stroke-width="1.5"/><path d="M4 9l3 3 10-11" fill="none" stroke="#e01f26" stroke-width="3"/></svg>MACKAY &amp; BOWEN BASIN</li>
    <li><svg viewBox="0 0 19 17"><rect x="1" y="3" width="12" height="12" fill="#fff" stroke="#e01f26" stroke-width="1.5"/><path d="M4 9l3 3 10-11" fill="none" stroke="#e01f26" stroke-width="3"/></svg>TOOWOOMBA &amp; SURAT BASIN</li>
  </ul>

  <div class="brand">
    <div class="brand-name"><span class="brand-mark"></span>HARBOURLINE PROPERTY PTY LTD</div>
    <div class="brand-tagline">Identifying <em>HOT</em> property for you……</div>
    <div class="brand-web">www.RentYieldQld.net.au</div>
  </div>

  <section class="contact-band">
    <div class="contact-tab"><span>CONTACT</span></div>
  </section>
  <div class="portrait" role="img" aria-label="Portrait photo of the company CEO in suit and red tie"></div>
  <div class="contact-details">
    <div class="contact-name">Warren Tolley</div>
    <div class="contact-role">CEO &amp; Licensee</div>
    <div class="contact-row"><b>email:</b> tolley@coralmail.net.au</div>
    <div class="contact-row"><b>phone:</b> 0400 555 018</div>
    <div class="contact-row"><b>office:</b> Brisbane &amp; Ipswich</div>
  </div>

  <div class="cta-bar">REQUEST YOUR FREE INVESTMENT KIT AND INDICATIVE CASHFLOW NOW!</div>
</main>
</body>
</html>
```